Service Offering Graphic Design

We need a small graphic designed which can be placed on our website, flyers etc. to outline our service offering - Hopefully this is a very simple task.

It needs to be professional and business oriented.

I have attached two pictures:
Picture1 shows our two high level services and the composition of each below it. Underpinning both is the following statements:
"Contextual"
"Vendor Agnostic"
You can place these words to represent that approach as you feel fits.

Picture titled 'quad' - an example from another company (not as something we would like you to copy). Its to show someone and say ' high level, this is what we do'.

No background please - It exists to be embedded as a png most likely.

Font on our website is Sans Serif - Could we continue this is in the graphic.

Target Market(s)

Other business

Industry/Entity Type

Defence

Font styles to use
Sans Serif

Colors

Designer to choose colors to be used in the design.

Requirements
Must have
• The text
Should not have
• Little logos of men or light bulbs
• Logo is added for detail on colour only.

```html
<!DOCTYPE html>
<html lang="en">
<head>
<meta charset="utf-8">
<title>Service Offering – Colour Options</title>
<link rel="stylesheet" href="https://fonts.googleapis.com/css2?family=Roboto+Condensed:wght@400;700&display=swap">
<style>
  :root {
    --red: #d7262e;
    --black: #161616;
    --dark: #3a3a3c;
    --grey: #6d6e70;
    --white: #ffffff;
    --ink: #1a1a1a;
  }
  html, body {
    margin: 0;
    padding: 0;
    width: 795px;
    height: 1200px;
    overflow: hidden;
    background: var(--white);
    font-family: "Roboto Condensed", Arial, sans-serif;
  }
  .sheet { display: block; width: 795px; height: 1200px; }
  .option-label { font-size: 12px; font-weight: 700; fill: var(--ink); }
  .bar-text { font-size: 8px; font-weight: 700; fill: var(--white); letter-spacing: 0.3px; }
  .services-text { font-size: 11px; font-weight: 700; fill: var(--white); letter-spacing: 3px; }
  .column-text { font-size: 6.6px; font-weight: 700; fill: var(--white); }
  .approach-text { font-size: 10px; font-weight: 700; fill: var(--ink); letter-spacing: 0.6px; }
  .brand-name { font-size: 11px; font-weight: 700; fill: var(--ink); letter-spacing: 1.5px; }
  .brand-square { fill: var(--red); }
  .bar { fill: var(--bar); }
  .services-bar { fill: var(--svc); }
  .column-cell { fill: var(--col); }
  .step-dot { fill: var(--num); }
  .step-num { font-size: 8px; font-weight: 700; fill: var(--white); }

  .scheme-1 { --bar: var(--red);  --svc: var(--black); --col: var(--dark);  --num: var(--red); }
  .scheme-2 { --bar: var(--red);  --svc: var(--black); --col: var(--black); --num: var(--red); }
  .scheme-3 { --bar: var(--red);  --svc: var(--grey);  --col: var(--dark);  --num: var(--red); }
  .scheme-4 { --bar: var(--dark); --svc: var(--grey);  --col: var(--black); --num: var(--dark); }
  .scheme-5 { --bar: var(--dark); --svc: var(--red);   --col: var(--black); --num: var(--dark); }
  .scheme-6 { --bar: var(--grey); --svc: var(--black); --col: var(--red);   --num: var(--grey); }
</style>
</head>
<body>
<svg class="sheet" viewBox="0 0 795 1200" xmlns="http://www.w3.org/2000/svg">
  <defs>
    <g id="service-diagram">
      <!-- contextual (left) offerings -->
      <polygon class="bar" points="60,30 285,30 335,72 335,75.2 285,44 60,44"/>
      <polygon class="bar" points="60,48 285,48 335,75.6 335,78.8 285,62 60,62"/>
      <polygon class="bar" points="60,66 285,66 335,79.2 335,82.4 285,80 60,80"/>
      <polygon class="bar" points="60,84 285,84 335,82.8 335,86 285,98 60,98"/>
      <text class="bar-text" x="70" y="40">SYSTEM DESIGN &amp; INTEGRATION</text>
      <text class="bar-text" x="70" y="58">REQUIREMENTS ENGINEERING</text>
      <text class="bar-text" x="70" y="76">TEST &amp; EVOLUTION</text>
      <text class="bar-text" x="70" y="94">TRAINING &amp; SUPPORT</text>

      <!-- vendor agnostic (right) offerings -->
      <polygon class="bar" points="735,30 510,30 460,72 460,75.2 510,44 735,44"/>
      <polygon class="bar" points="735,48 510,48 460,75.6 460,78.8 510,62 735,62"/>
      <polygon class="bar" points="735,66 510,66 460,79.2 460,82.4 510,80 735,80"/>
      <polygon class="bar" points="735,84 510,84 460,82.8 460,86 510,98 735,98"/>
      <text class="bar-text" x="520" y="40">MARKET INVESTIGATION</text>
      <text class="bar-text" x="520" y="58">IDEA GENERATION &amp; SCREENING</text>
      <text class="bar-text" x="520" y="76">PROTOTYPING</text>
      <text class="bar-text" x="520" y="94">CONCEPTS DEVELOPMENT</text>

      <!-- brand -->
      <rect class="brand-square" x="346" y="36" width="22" height="22"/>
      <text class="brand-name" x="374" y="46">HARLOW</text>
      <text class="brand-name" x="374" y="58">DEFENCE</text>

      <!-- services -->
      <rect class="services-bar" x="335" y="72" width="125" height="14"/>
      <text class="services-text" x="397.5" y="82.5" text-anchor="middle">SERVICES</text>
      <rect class="column-cell" x="335" y="88" width="61.5" height="22"/>
      <rect class="column-cell" x="398.5" y="88" width="61.5" height="22"/>
      <text class="column-text" x="365.7" y="97" text-anchor="middle">CAPABILITY</text>
      <text class="column-text" x="365.7" y="105" text-anchor="middle">DEVELOPMENT</text>
      <text class="column-text" x="429.2" y="97" text-anchor="middle">RESEARCH AND</text>
      <text class="column-text" x="429.2" y="105" text-anchor="middle">DEVELOPMENT</text>

      <!-- approach -->
      <text class="approach-text" x="175" y="120" text-anchor="middle">CONTEXTUAL</text>
      <text class="approach-text" x="620" y="120" text-anchor="middle">VENDOR AGNOSTIC</text>
    </g>

    <g id="step-numbers">
      <circle class="step-dot" cx="44" cy="37" r="7"/><text class="step-num" x="44" y="40" text-anchor="middle">1</text>
      <circle class="step-dot" cx="44" cy="55" r="7"/><text class="step-num" x="44" y="58" text-anchor="middle">2</text>
      <circle class="step-dot" cx="44" cy="73" r="7"/><text class="step-num" x="44" y="76" text-anchor="middle">3</text>
      <circle class="step-dot" cx="44" cy="91" r="7"/><text class="step-num" x="44" y="94" text-anchor="middle">4</text>
      <circle class="step-dot" cx="751" cy="37" r="7"/><text class="step-num" x="751" y="40" text-anchor="middle">1</text>
      <circle class="step-dot" cx="751" cy="55" r="7"/><text class="step-num" x="751" y="58" text-anchor="middle">2</text>
      <circle class="step-dot" cx="751" cy="73" r="7"/><text class="step-num" x="751" y="76" text-anchor="middle">3</text>
      <circle class="step-dot" cx="751" cy="91" r="7"/><text class="step-num" x="751" y="94" text-anchor="middle">4</text>
    </g>
  </defs>

  <g class="option scheme-1" transform="translate(0,8)">
    <text class="option-label" x="8" y="14">Option 1</text>
    <use href="#service-diagram"/>
    <use href="#step-numbers"/>
  </g>

  <g class="option scheme-2" transform="translate(0,205)">
    <text class="option-label" x="8" y="14">Option 2</text>
    <use href="#service-diagram"/>
  </g>

  <g class="option scheme-3" transform="translate(0,402)">
    <text class="option-label" x="8" y="14">Option 3</text>
    <use href="#service-diagram"/>
    <use href="#step-numbers"/>
  </g>

  <g class="option scheme-4" transform="translate(0,599)">
    <text class="option-label" x="8" y="14">Option 4</text>
    <use href="#service-diagram"/>
    <use href="#step-numbers"/>
  </g>

  <g class="option scheme-5" transform="translate(0,796)">
    <text class="option-label" x="8" y="14">Option 5</text>
    <use href="#service-diagram"/>
  </g>

  <g class="option scheme-6" transform="translate(0,993)">
    <text class="option-label" x="8" y="14">Option 6</text>
    <use href="#service-diagram"/>
  </g>
</svg>
</body>
</html>
```